Branding Postcard for Real Estate Brokerage

I am a Real Estate Broker looking for a template postcard that I can use with lots of types of situations , solds, listed property, etc but has a standard layout that is consistent so it will be recognizable and tied to me. There was one that was on the template group that caught my eye. I was thinking of using the A in my logo as the script or watermark. I have uploaded my idea on that as well as other logos, etc. My goal is to have a template that I can add text to and market different things / sales / request action for pricing, etc.

Target Market(s)

Homeowners in Neighborhoods where I have sold homes

Industry/Entity Type

Real Estate

Requirements
Must have
• Area to add label for mailing, Area in front has to be a template where I can write specifics of the mailing, Consistent branding

```html
<!DOCTYPE html>
<html lang="en">
<head>
<meta charset="utf-8">
<title>Harborline Realty Group – Postcard</title>
<link href="https://fonts.googleapis.com/css2?family=Marcellus&family=Questrial&display=swap" rel="stylesheet">
<style>
  :root {
    --navy-deep: #1b1a5c;
    --navy-mid: #272878;
    --navy-bright: #3b3ca6;
    --paper: #ffffff;
    --ink: #111111;
    --photo-sky: #7fa9d6;
    --photo-lawn: #5f8a3a;
    --photo-stone: #b9b2a4;
    --photo-house: #8a6f55;
  }
  html, body {
    margin: 0;
    padding: 0;
    overflow: hidden;
  }
  body {
    width: 775px;
    height: 1200px;
    background: var(--paper);
    position: relative;
    font-family: "Questrial", "Century Gothic", sans-serif;
    color: var(--ink);
  }
  .card {
    position: absolute;
    left: 16px;
    width: 734px;
    background: var(--paper);
    outline: 1px solid #d8d8e4;
    overflow: hidden;
  }
  .band {
    position: absolute;
    left: 0;
    width: 100%;
    background: linear-gradient(90deg, var(--navy-deep) 0%, var(--navy-mid) 55%, var(--navy-bright) 100%);
  }

  /* Front */
  .card--front { top: 13px; height: 570px; }
  .card--front .band--top { top: 0; height: 145px; }
  .card--front .band--bottom { bottom: 0; height: 50px; }
  .headline {
    position: absolute;
    left: 38px;
    top: 26px;
    margin: 0;
    font-family: "Marcellus", "Optima", serif;
    font-weight: 400;
    font-size: 72px;
    letter-spacing: 1px;
    color: #e6e6ee;
  }
  .offer {
    position: absolute;
    left: 45px;
    top: 162px;
    margin: 0;
    font-size: 32px;
    font-weight: 400;
  }
  .brokerage {
    position: absolute;
    left: 43px;
    top: 340px;
    margin: 0;
    font-size: 34px;
    line-height: 41px;
    font-weight: 400;
  }
  .phone {
    position: absolute;
    left: 45px;
    top: 432px;
    margin: 0;
    font-size: 29px;
  }
  .photo {
    position: absolute;
    left: 430px;
    width: 275px;
    box-shadow: 3px 4px 6px rgba(0,0,0,0.45);
  }
  .photo--modern {
    top: 158px;
    height: 169px;
    background: linear-gradient(180deg, var(--photo-sky) 0%, #e9eef3 45%, var(--photo-lawn) 72%, var(--photo-stone) 100%);
  }
  .photo--craftsman {
    top: 340px;
    height: 170px;
    background: linear-gradient(180deg, var(--photo-sky) 0%, var(--photo-house) 40%, #6e5d4c 68%, var(--photo-lawn) 100%);
  }

  /* Back */
  .card--back { top: 614px; height: 573px; }
  .card--back .band--top { top: 0; height: 123px; }
  .card--back .band--bottom { bottom: 0; height: 57px; }
  .return-name {
    position: absolute;
    left: 48px;
    top: 28px;
    margin: 0;
    font-size: 34px;
    line-height: 42px;
    font-weight: 400;
    color: #f2f2f7;
  }
  .address-line {
    position: absolute;
    left: 0;
    top: 123px;
    width: 100%;
    height: 51px;
  }
  .address-line .label {
    position: absolute;
    left: 32px;
    top: 9px;
    font-size: 29px;
  }
  .rule {
    position: absolute;
    left: 0;
    top: 174px;
    width: 100%;
    height: 10px;
    background: linear-gradient(90deg, var(--navy-deep), var(--navy-bright));
  }
</style>
</head>
<body>
  <section class="card card--front">
    <div class="band band--top"></div>
    <h1 class="headline">JUST SOLD</h1>
    <p class="offer">Special Offer</p>
    <p class="brokerage">Harborline Realty<br>Group</p>
    <p class="phone">555-014-2287</p>
    <div class="photo photo--modern" role="img" aria-label="Photo of a modern white villa with a paved driveway and green lawn"></div>
    <div class="photo photo--craftsman" role="img" aria-label="Photo of a two-storey craftsman-style house with a front porch and garden"></div>
    <div class="band band--bottom"></div>
  </section>

  <section class="card card--back">
    <div class="band band--top"></div>
    <p class="return-name">Harborline Realty<br>Group</p>
    <div class="address-line"><span class="label">To:</span></div>
    <div class="rule"></div>
    <div class="band band--bottom"></div>
  </section>
</body>
</html>
```